Business Card for a mobile physiotherapy company

I need a layout for a business card for a mobile physiotherapy company.
Slogan is "Mobile Physiotherapy - Your Road To Recovery"
Phone number is 867-402-5913
Email VantrePhysio@mailbright.ca (subject to change with website)
Website www.VantrePhysio.ca
My name and credentials: Kent Vantre Kent Vantre, BSc(kin), MPT, CAFCI, IMS
Information maybe included: Direct Billing, Services including Physiotherapy, IMS, acupuncture
Maybe include facebook and instagram logos
One side with the logo clean and sharp
Other side with details, try not to look too busy, keep everything concise

```html
<!DOCTYPE html>
<html lang="en">
<head>
<meta charset="utf-8">
<title>Vantre Therapy – Business Card</title>
<link href="https://fonts.googleapis.com/css2?family=Lato:wght@400;700&family=Tinos:wght@400;700&display=swap" rel="stylesheet">
<style>
  :root {
    --bg: #e4e5e8;
    --card-white: #ffffff;
    --navy: #2c4a72;
    --navy-text: #2d4470;
    --rule: #d5d9e0;
    --on-navy: #ffffff;
    --on-navy-rule: rgba(255,255,255,0.55);
    --shadow: 0 10px 28px rgba(0,0,0,0.18);
  }
  * { margin: 0; padding: 0; box-sizing: border-box; }
  html, body { width: 1200px; height: 900px; overflow: hidden; }
  body {
    background: var(--bg);
    position: relative;
    font-family: "Lato", Arial, sans-serif;
  }
  .card {
    position: absolute;
    width: 560px;
    height: 320px;
    border-radius: 28px;
    box-shadow: var(--shadow);
    display: flex;
    flex-direction: column;
    align-items: center;
  }
  /* Front */
  .card--front {
    left: 60px; top: 110px;
    background: var(--card-white);
    justify-content: center;
  }
  .brand {
    display: flex;
    align-items: center;
    gap: 14px;
    margin-top: 10px;
  }
  .brand__dot {
    width: 22px; height: 22px;
    background: var(--navy);
    border-radius: 50%;
  }
  .brand__name {
    font-family: "Tinos", "Times New Roman", serif;
    font-weight: 700;
    font-size: 46px;
    letter-spacing: 4px;
    color: var(--navy-text);
    text-transform: uppercase;
  }
  .social {
    display: flex;
    gap: 8px;
    margin-top: 22px;
  }
  .social__dot {
    width: 18px; height: 18px;
    border-radius: 50%;
    background: var(--navy);
  }
  .slogan {
    margin-top: 12px;
    padding-top: 10px;
    border-top: 1px solid var(--rule);
    width: 430px;
    text-align: center;
    font-size: 14px;
    letter-spacing: 0.5px;
    color: var(--navy-text);
    text-transform: uppercase;
  }
  /* Back */
  .card--back {
    left: 580px; top: 470px;
    background: var(--navy);
    color: var(--on-navy);
    justify-content: center;
    text-align: center;
  }
  .person {
    font-family: "Tinos", "Times New Roman", serif;
  }
  .person__name {
    font-weight: 700;
    font-size: 21px;
    text-transform: uppercase;
  }
  .person__creds {
    font-size: 15px;
    text-transform: uppercase;
  }
  .divider {
    display: flex;
    align-items: center;
    gap: 10px;
    margin: 10px 0 6px;
    font-size: 15px;
    letter-spacing: 1px;
  }
  .divider::before, .divider::after {
    content: "";
    width: 70px;
    height: 1px;
    background: var(--on-navy-rule);
  }
  .icons { display: flex; gap: 4px; }
  .icons svg { width: 18px; height: 18px; }
  .contact {
    list-style: none;
    font-size: 16px;
    line-height: 1.25;
  }
  .services {
    font-size: 16px;
    line-height: 1.3;
  }
</style>
</head>
<body>

<section class="card card--front">
  <div class="brand">
    <span class="brand__dot"></span>
    <span class="brand__name">Vantre Therapy</span>
  </div>
  <div class="social">
    <span class="social__dot"></span>
    <span class="social__dot"></span>
  </div>
  <p class="slogan">Mobile Physiotherapy - Your Road to Recovery</p>
</section>

<section class="card card--back">
  <p class="person">
    <span class="person__name">Kent Vantre,</span>
    <span class="person__creds">BSc(Kin), MPT, CAFCI, IMS</span>
  </p>

  <div class="divider">
    <span class="icons">
      <svg viewBox="0 0 18 18" aria-label="phone">
        <rect x="0.5" y="0.5" width="17" height="17" rx="2" fill="#fff"/>
        <path d="M5 4.5c1 0 1.6 2 1.2 2.6l-.7.7c.6 1.4 1.6 2.4 3 3l.7-.7c.6-.4 2.6.2 2.6 1.2 0 1-1 2-2 2C6.6 13.3 4.7 11.4 3 7.5c0-1 1-3 2-3z" fill="var(--navy)"/>
      </svg>
      <svg viewBox="0 0 18 18" aria-label="email">
        <rect x="0.5" y="0.5" width="17" height="17" rx="2" fill="#fff"/>
        <rect x="3.5" y="5" width="11" height="8" fill="none" stroke="var(--navy)" stroke-width="1.3"/>
        <path d="M3.5 5l5.5 4.5L14.5 5" fill="none" stroke="var(--navy)" stroke-width="1.3"/>
      </svg>
      <svg viewBox="0 0 18 18" aria-label="website">
        <rect x="0.5" y="0.5" width="17" height="17" rx="2" fill="#fff"/>
        <circle cx="9" cy="9" r="5" fill="none" stroke="var(--navy)" stroke-width="1.2"/>
        <ellipse cx="9" cy="9" rx="2.2" ry="5" fill="none" stroke="var(--navy)" stroke-width="1"/>
        <path d="M4 9h10" stroke="var(--navy)" stroke-width="1"/>
      </svg>
    </span>
  </div>

  <ul class="contact">
    <li>867-402-5913</li>
    <li>VantrePhysio@mailbright.ca</li>
    <li>www.VantrePhysio.ca</li>
  </ul>

  <div class="divider">SERVICES</div>

  <p class="services">
    Direct Billing &nbsp;|&nbsp; Services including Physiotherapy<br>
    IMS | acupuncture
  </p>
</section>

</body>
</html>
```